Vornel Technologies business card design

We need a business card designed with our new logo. it would be great if the card could communicate it is a technology based company.

Target Market(s)

system integrators

Industry/Entity Type

technology, IOT

Contact Information for Business Card

Name, designation, Address, telephone number, email address

Requirements
Must have
• logo and company name
Nice to have
• something to do with technology

```html
<!DOCTYPE html>
<html lang="en">
<head>
<meta charset="UTF-8">
<title>Vornel Technologies – Business Card</title>
<link href="https://fonts.googleapis.com/css2?family=Montserrat:wght@400;500;700&family=Saira:wght@700&display=swap" rel="stylesheet">
<style>
  :root {
    --card-black: #000000;
    --paper-white: #ffffff;
    --amber: #f7931e;
    --amber-deep: #8a5210;
    --amber-shadow: #3a2408;
    --text-white: #ffffff;
  }
  * { margin: 0; padding: 0; box-sizing: border-box; }
  html, body {
    width: 1034px; height: 1200px; overflow: hidden;
    background: var(--paper-white);
  }
  .sheet {
    width: 1034px; height: 1200px;
    display: flex; flex-direction: column; justify-content: space-between;
  }
  .card {
    position: relative; width: 1034px; height: 591px;
    background: var(--card-black); overflow: hidden;
    font-family: 'Montserrat', sans-serif; color: var(--text-white);
  }
  .pixel-band { position: absolute; inset: 0; width: 100%; height: 100%; }

  .brand {
    position: absolute; display: flex; align-items: center; gap: 16px;
    font-family: 'Montserrat', sans-serif; font-weight: 700;
    color: var(--text-white); letter-spacing: 1px; text-transform: uppercase;
    line-height: 1.1; white-space: nowrap;
  }
  .brand-name span { display: block; }
  .brand-square { background: var(--amber); flex: none; }
  .card-front .brand {
    left: 240px; top: 320px; transform: translate(-50%, -50%);
    font-size: 30px;
  }
  .card-front .brand-square { width: 22px; height: 22px; }
  .card-back .brand {
    left: 517px; top: 300px; transform: translate(-50%, -50%);
    font-size: 42px;
  }
  .card-back .brand-square { width: 30px; height: 30px; }

  .person { position: absolute; left: 507px; top: 164px; width: 436px; }
  .person-name {
    font-family: 'Saira', sans-serif; font-weight: 700;
    font-size: 50px; line-height: 1; letter-spacing: 0.5px;
  }
  .person-role { font-size: 24px; font-weight: 500; margin-top: 12px; line-height: 1.2; }
  .person-rule { height: 3px; background: var(--amber); margin-top: 16px; }
  .contact-list { list-style: none; margin-top: 20px; }
  .contact-item {
    display: flex; align-items: center; gap: 24px;
    font-size: 21px; font-weight: 500; height: 50px;
  }
  .contact-icon { width: 18px; height: 18px; fill: var(--text-white); flex: none; }
</style>
</head>
<body>
<main class="sheet">
  <section class="card card-front">
    <svg class="pixel-band" viewBox="0 0 1034 591" role="img" aria-label="Diagonal bands of scattered amber pixel squares in the corners">
      <defs>
        <linearGradient id="bandTop" x1="0" y1="0" x2="1" y2="0.6">
          <stop offset="0" stop-color="#8a5210"/>
          <stop offset="1" stop-color="#3a2408" stop-opacity="0"/>
        </linearGradient>
        <linearGradient id="bandBottom" x1="1" y1="1" x2="0" y2="0.4">
          <stop offset="0" stop-color="#8a5210"/>
          <stop offset="1" stop-color="#3a2408" stop-opacity="0"/>
        </linearGradient>
      </defs>
      <polygon points="0,0 510,0 300,110 0,220" fill="url(#bandTop)"/>
      <polygon points="1034,360 1034,591 520,591 760,470" fill="url(#bandBottom)"/>
    </svg>

    <div class="brand">
      <span class="brand-square"></span>
      <div class="brand-name"><span>Vornel</span><span>Technologies</span></div>
    </div>

    <div class="person">
      <h1 class="person-name">YOUR NAME</h1>
      <p class="person-role">Designation</p>
      <div class="person-rule"></div>
      <ul class="contact-list">
        <li class="contact-item">
          <svg class="contact-icon" viewBox="0 0 24 24"><path d="M12 1a8 8 0 0 0-8 8c0 6 8 14 8 14s8-8 8-14a8 8 0 0 0-8-8zm0 11a3 3 0 1 1 0-6 3 3 0 0 1 0 6z"/></svg>
          <span>your address xyz</span>
        </li>
        <li class="contact-item">
          <svg class="contact-icon" viewBox="0 0 24 24"><path d="M6.6 10.8a15 15 0 0 0 6.6 6.6l2.2-2.2a1 1 0 0 1 1-.25 11.4 11.4 0 0 0 3.6.6 1 1 0 0 1 1 1V20a1 1 0 0 1-1 1A17 17 0 0 1 3 4a1 1 0 0 1 1-1h3.5a1 1 0 0 1 1 1c0 1.25.2 2.45.6 3.6a1 1 0 0 1-.25 1z"/></svg>
          <span>0000 000 000</span>
        </li>
        <li class="contact-item">
          <svg class="contact-icon" viewBox="0 0 24 24"><path d="M1 5h22v14H1zM2.5 6.5 12 13.5l9.5-7z" fill-rule="evenodd"/></svg>
          <span>info@mail.com</span>
        </li>
      </ul>
    </div>
  </section>

  <section class="card card-back">
    <svg class="pixel-band" viewBox="0 0 1034 591" role="img" aria-label="Diagonal bands of scattered amber pixel squares in the corners">
      <polygon points="0,0 510,0 300,110 0,220" fill="url(#bandTop)"/>
      <polygon points="1034,360 1034,591 520,591 760,470" fill="url(#bandBottom)"/>
    </svg>
    <div class="brand">
      <span class="brand-square"></span>
      <div class="brand-name"><span>Vornel</span><span>Technologies</span></div>
    </div>
  </section>
</main>
</body>
</html>
```